Book cover design for a collection of poetry - The Lanternfield

Book cover and back design need to be moody, nostalgic, reflective, ethereal. Melancholy and other worldly. Cover design should not be time specific to a period or place but if applicable should reflect British landscape. Book cover should be in tones of blue and must include the title and author (THE LANTERNFIELD BY DORIAN WELKBRIDGE). We love the idea of rain, and looking out of a window. See attached designs. A world you are observing but not in.

Industry/Entity Type

Book Publisher

Font styles to use
Serif
Script

Colors
3176b5
3377b5
85acd3
eaf1f7
0792cd
33a6d7
86cae7
ecf7fb
86cfc6

Requirements
Must have
• The colour blue in it, must be melancholy and reflective.
Nice to have
• Rain in the cover.
Should not have
• Any bright colours.

```html
<!DOCTYPE html>
<html lang="en">
<head>
<meta charset="utf-8">
<title>The Lanternfield — Cover Spread</title>
<link rel="stylesheet" href="https://fonts.googleapis.com/css2?family=Sorts+Mill+Goudy&family=Pinyon+Script&family=EB+Garamond:wght@400&display=swap">
<style>
  :root {
    --page: #ffffff;
    --frame-line: #c9c9c9;
    --navy: #1f3a57;
    --ink: #090c10;
    --front-edge: #223d5b;
    --cyan-text: #3fd6e4;
    --rule: #3fb9b0;
    --white: #ffffff;
    --label: #8a8a8a;
    --art-deep: #0f2f7a;
    --art-mid: #1e5cc0;
    --art-teal: #2aa7a0;
  }
  * { margin: 0; padding: 0; box-sizing: border-box; }
  html, body { width: 1200px; height: 985px; overflow: hidden; background: var(--page); }
  .canvas {
    position: relative; width: 1200px; height: 985px;
    border: 1px solid var(--frame-line); background: var(--page);
  }
  .spread {
    position: absolute; left: 61px; top: 82px; width: 1077px; height: 819px;
    border: 1px solid #000;
    background: linear-gradient(90deg, var(--navy) 0%, #111a26 30%, var(--ink) 48%, var(--ink) 53%, #0e151f 62%, var(--front-edge) 100%);
  }
  .spine-guide {
    position: absolute; left: 513px; top: 0; width: 51px; height: 100%;
    border-left: 1px solid #14313f; border-right: 1px solid #14313f;
  }
  .back-copy { position: absolute; left: 107px; top: 127px; color: var(--cyan-text); font-family: "Sorts Mill Goudy", serif; white-space: nowrap; }
  .back-title { font-size: 23px; line-height: 45px; font-weight: 400; }
  .back-blurb { margin-top: 17px; font-size: 14.6px; line-height: 24.2px; }
  .back-themes { margin-top: 41px; font-size: 14.6px; line-height: 23.8px; }
  .spine-text {
    position: absolute; left: 538px; top: 240px;
    transform: rotate(90deg); transform-origin: 0 0;
    white-space: nowrap; color: var(--cyan-text);
  }
  .spine-title { position: absolute; left: 0; top: -26px; font-family: "Pinyon Script", cursive; font-size: 27px; }
  .spine-author { position: absolute; left: 235px; top: -20px; font-family: "EB Garamond", serif; font-size: 15px; }
  .cover-art {
    position: absolute; left: 606px; top: 51px; width: 434px; height: 695px;
    border: 3px solid #000; border-radius: 38px; overflow: hidden;
    background:
      radial-gradient(ellipse at 30% 20%, rgba(42,167,160,.55), transparent 55%),
      radial-gradient(ellipse at 80% 70%, rgba(30,92,192,.6), transparent 60%),
      linear-gradient(180deg, var(--art-mid) 0%, var(--art-deep) 55%, #0a2256 100%);
  }
  .window-bar { position: absolute; background: #05090c; }
  .bar-vertical { left: 275px; top: 0; width: 15px; height: 100%; }
  .bar-horizontal { left: 0; top: 481px; width: 100%; height: 16px; }
  .cover-author {
    position: absolute; left: 0; right: 0; bottom: 20px; text-align: center;
    font-family: "EB Garamond", serif; font-size: 25px; color: var(--white);
  }
  .overlay { position: absolute; left: 0; top: 0; }
  .cover-title {
    position: absolute; left: 734px; top: 226px; white-space: nowrap;
    font-family: "Pinyon Script", cursive; font-size: 50px; line-height: 1; color: var(--white);
  }
  .label { position: absolute; top: 925px; font-family: "Sorts Mill Goudy", serif; font-size: 14px; color: var(--label); }
  .label-back { left: 302px; }
  .label-front { left: 864px; }
  .label-spine { left: 607px; top: 922px; transform: rotate(90deg); transform-origin: 0 0; }
</style>
</head>
<body>
<div class="canvas">
  <div class="spread">
    <div class="spine-guide"></div>

    <div class="back-copy">
      <h2 class="back-title">The Lanternfield<br>Is A Collection Of Poetry.</h2>
      <p class="back-blurb">Told In Two Parts We First Meet Charles –<br>Aged, Crippled And Left Alone In His<br>Inherited Marsh House - Reflecting On His<br>Life And His Marriage To Beautiful Alice<br>Who We Meet Inpart Two. Alice Is Suicidal,<br>Manically Depressed And Struggling With<br>Life As A Wife And Mother. She Meets,<br>Harbors And Falls In Love With A Soldier<br>During WwII And Her World Is Changed<br>Forever.</p>
      <p class="back-themes">Moving Through The 20th Century,<br>This Life And The Next, The Lanternfield Interweaves<br>Grief, Loss, The After-life, Mental Illness,<br>And Ultimately The True Nature Of Love.</p>
    </div>

    <div class="spine-text">
      <span class="spine-title">The Lanternfield</span>
      <span class="spine-author">By Dorian Welkbridge</span>
    </div>

    <div class="cover-art" role="img" aria-label="Abstract painting of rain-streaked blue and teal woodland seen through a window">
      <div class="window-bar bar-vertical"></div>
      <div class="window-bar bar-horizontal"></div>
      <div class="cover-author">By Dorian Welkbridge</div>
    </div>
  </div>

  <svg class="overlay" width="1200" height="985" viewBox="0 0 1200 985" aria-hidden="true">
    <line x1="168" y1="247" x2="1031" y2="247" stroke="var(--rule)" stroke-width="1"/>
    <line x1="168" y1="295" x2="1031" y2="295" stroke="var(--rule)" stroke-width="1"/>
  </svg>
  <div class="cover-title">The Lanternfield</div>

  <span class="label label-back">Back</span>
  <span class="label label-spine">Spine</span>
  <span class="label label-front">Front</span>
</div>
</body>
</html>
```